LUMEN TRUSTEES LTD.
STATIONERY DESIGN
LUMEN TRUSTEES LTD. - Financial Services
Simple
MOIRA ELLSWORTH
SENIOR EXECUTIVE ADVISOR
42 MARLOWE ST, NASSAU, N.P., THE BAHAMAS
moira@lumentrusteesltd.net
www.lumen.bs and/or www.lumentrusteesltd.net
can I get a bar code to scan my business card?
MoiraE MoiraE
Hi all. I am receiving logos for the incorrect company. I am requesting logs for LUMEN TRUSTESE LTD. (blue and range logo), as well as the stationary layout which is a priority at this time. Please send stationery and business card for Lumen Trustees Ltd. I will review the pink Tin Kettle business card and stationery and if I choose any, I will pay for that as well. Thanks

```html
<!DOCTYPE html>
<html lang="en">
<head>
<meta charset="utf-8">
<title>Lumen Trustees Ltd. – Business Card</title>
<link rel="stylesheet" href="https://fonts.googleapis.com/css2?family=Montserrat:wght@500;600;700;800&display=swap">
<style>
  :root {
    --page: #ffffff;
    --card-dark: #17161d;
    --card-mid: #2c2b3a;
    --card-light: #4b4968;
    --green: #a9ea5e;
    --gold: #f2c94c;
    --white: #f4f4f7;
    --icon-ink: #1c1b24;
  }
  * { margin: 0; padding: 0; box-sizing: border-box; }
  html, body {
    width: 1200px; height: 961px; overflow: hidden;
    background: var(--page);
    font-family: "Montserrat", sans-serif;
  }
  .canvas { position: relative; width: 1200px; height: 961px; }

  .card {
    position: absolute;
    width: 777px; height: 461px;
    overflow: hidden;
  }
  .card--front { left: 0; top: 0; }
  .card--back { left: 420px; top: 497px; }

  .card__pattern {
    position: absolute; inset: 0;
    background: linear-gradient(100deg, var(--card-dark) 0%, var(--card-mid) 45%, var(--card-light) 100%);
  }

  .holder__name {
    position: absolute; left: 92px; top: 122px;
    color: var(--green);
    font-weight: 800; font-size: 33px; letter-spacing: 1px;
  }
  .holder__title {
    position: absolute; left: 94px; top: 170px;
    color: var(--gold);
    font-weight: 700; font-size: 14px; letter-spacing: 3px;
  }

  .contact { position: absolute; left: 96px; top: 214px; list-style: none; }
  .contact__item {
    display: flex; align-items: flex-start; gap: 12px;
    color: var(--white);
    font-weight: 500; font-size: 13px; line-height: 16px;
    text-transform: uppercase;
    margin-bottom: 17px;
  }
  .contact__item--wide { margin-bottom: 14px; }
  .contact__icon {
    flex: none; width: 18px; height: 18px; border-radius: 3px;
    display: flex; align-items: center; justify-content: center;
  }
  .contact__icon--green { background: var(--green); }
  .contact__icon--gold { background: var(--gold); }
  .contact__web { font-size: 11px; line-height: 13px; }

  .brand-name {
    position: absolute;
    display: flex; align-items: center; gap: 14px;
    color: var(--green);
    font-weight: 700; letter-spacing: 2px;
  }
  .brand-name__mark { flex: none; background: var(--gold); }
  .card--front .brand-name { left: 520px; top: 176px; font-size: 19px; line-height: 24px; }
  .card--front .brand-name__mark { width: 34px; height: 34px; }

  .card__question {
    position: absolute; left: 96px; top: 420px;
    color: var(--green);
    font-weight: 600; font-size: 17px; letter-spacing: 1.2px;
    text-transform: uppercase;
  }

  .card--back .brand-name { left: 170px; top: 170px; font-size: 30px; line-height: 44px; gap: 28px; letter-spacing: 4px; }
  .card--back .brand-name__mark { width: 118px; height: 118px; }
</style>
</head>
<body>
<main class="canvas">

  <section class="card card--front" aria-label="Business card front">
    <div class="card__pattern" role="img" aria-label="Dark navy to violet background with a faint isometric cube pattern"></div>

    <h1 class="holder__name">MOIRA ELLSWORTH</h1>
    <p class="holder__title">SENIOR EXECUTIVE ADVISOR</p>

    <ul class="contact">
      <li class="contact__item">
        <span class="contact__icon contact__icon--green">
          <svg width="12" height="10" viewBox="0 0 12 10"><rect x="0.5" y="0.5" width="11" height="9" fill="none" stroke="var(--icon-ink)" stroke-width="1.2"/><path d="M0.5 0.8 L6 5.5 L11.5 0.8" fill="none" stroke="var(--icon-ink)" stroke-width="1.2"/></svg>
        </span>
        <span>moira@lumentrusteesltd.net</span>
      </li>
      <li class="contact__item">
        <span class="contact__icon contact__icon--gold">
          <svg width="12" height="12" viewBox="0 0 12 12"><path d="M2.5 1 L4.5 1 L5.3 3.6 L4 4.6 C4.7 6 6 7.3 7.4 8 L8.4 6.7 L11 7.5 L11 9.5 C11 10.3 10.3 11 9.5 11 C5 11 1 7 1 2.5 C1 1.7 1.7 1 2.5 1 Z" fill="var(--icon-ink)"/></svg>
        </span>
        <span>+12425550147</span>
      </li>
      <li class="contact__item contact__item--wide">
        <span class="contact__icon contact__icon--green">
          <svg width="10" height="13" viewBox="0 0 10 13"><path d="M5 0.5 C7.5 0.5 9.5 2.4 9.5 4.8 C9.5 8 5 12.5 5 12.5 C5 12.5 0.5 8 0.5 4.8 C0.5 2.4 2.5 0.5 5 0.5 Z" fill="var(--icon-ink)"/><circle cx="5" cy="4.8" r="1.6" fill="var(--green)"/></svg>
        </span>
        <span>42 Marlowe St, Nassau, N.P.,<br>The Bahamas</span>
      </li>
      <li class="contact__item">
        <span class="contact__icon contact__icon--gold">
          <svg width="12" height="12" viewBox="0 0 12 12"><circle cx="6" cy="6" r="5" fill="none" stroke="var(--icon-ink)" stroke-width="1.1"/><ellipse cx="6" cy="6" rx="2.2" ry="5" fill="none" stroke="var(--icon-ink)" stroke-width="1"/><path d="M1 6 H11" stroke="var(--icon-ink)" stroke-width="1"/></svg>
        </span>
        <span class="contact__web">www.lumen.bs and/or<br>www.lumentrusteesltd.net</span>
      </li>
    </ul>

    <div class="brand-name">
      <span class="brand-name__mark"></span>
      <span>LUMEN<br>TRUSTEES LTD.</span>
    </div>

    <p class="card__question">Can I get a bar code to scan my business card?</p>
  </section>

  <section class="card card--back" aria-label="Business card back">
    <div class="card__pattern" role="img" aria-label="Dark navy to violet background with a faint isometric cube pattern"></div>

    <div class="brand-name">
      <span class="brand-name__mark"></span>
      <span>SENIOR<br>EXECUTIVE<br>ADVISOR</span>
    </div>
  </section>

</main>
</body>
</html>
```